Bref créative
Website template for salsa company
Abuela Rufina's Roasted Dip
Food
www.RoastedDipco.com
Startup salsa company. We aim to change peoples thinking that salsa is just for "Chips & Salsa". The website will contain recipes and ideas for using the salsa in others ways as well as an ecommerce page where you can buy it.
Dislike dark backgrounds
Like easy navigation
Like dynamic content
Like a little humor in pictures such characters (peppers that smile etc)
Colorful
Humorous
top
www.kendrawpepperjars.com
Rather than just using the 3 "primary" colors in the logo please fell free to use complimentary colors as well as the monochromatic colors for each of the 3.
I will answer any questions you may have.
Company logo
Mild pepper
Hispanic designs
Happy pepper
Mean looking pepper
3 peppers
3 peppers #2
3 peppers #3
flaming peppers
habanero pepper

```html
<!DOCTYPE html>
<html lang="en">
<head>
<meta charset="utf-8">
<title>Abuela Rufina's Roasted Dip — About Us</title>
<link rel="stylesheet" href="https://fonts.googleapis.com/css2?family=Arimo:wght@400;700&family=Sorts+Mill+Goudy&display=swap">
<style>
  :root {
    --green: #0d8a3a;
    --yellow: #f3c818;
    --orange: #ee8a1c;
    --red: #dc3b1c;
    --panel: #f8e6dc;
    --white: #ffffff;
    --ink: #1a1a1a;
    --icon-fill: #e7b43a;
    --photo-red: #9a2a22;
    --photo-light: #c9b7a8;
  }
  * { margin: 0; padding: 0; box-sizing: border-box; }
  html, body { width: 1200px; height: 751px; overflow: hidden; }
  body {
    position: relative;
    font-family: "Arimo", Arial, sans-serif;
    color: var(--ink);
    background: linear-gradient(180deg, var(--yellow) 0px, var(--yellow) 90px, var(--orange) 360px, var(--red) 700px);
  }
  .top-bar, .bottom-bar {
    position: absolute; left: 0; width: 1200px; background: var(--green);
    color: var(--white); font-weight: 700; font-size: 10px;
  }
  .top-bar { top: 0; height: 29px; }
  .bottom-bar { bottom: 0; height: 38px; }
  .contact-info { position: absolute; left: 922px; top: 9px; }
  .copyright { position: absolute; left: 0; right: 0; top: 13px; text-align: center; }

  .brand-panel {
    position: absolute; left: 113px; top: 0; width: 290px; height: 175px;
    background: var(--panel);
    clip-path: polygon(0 0, 100% 0, 94% 100%, 6% 100%);
    display: flex; align-items: center; justify-content: center; gap: 10px;
  }
  .brand-mark { width: 22px; height: 22px; border-radius: 50%; background: var(--green); flex: none; }
  .brand-name {
    font-family: "Sorts Mill Goudy", Georgia, serif;
    font-size: 25px; line-height: 1.05; color: var(--red); width: 200px;
  }

  .nav-panel {
    position: absolute; left: 137px; top: 187px; width: 247px; height: 231px;
    background: var(--panel);
  }
  .nav-list { list-style: none; position: absolute; left: 40px; top: 24px; }
  .nav-item {
    display: flex; align-items: center; height: 31.8px;
    font-weight: 700; font-size: 17px;
  }
  .nav-item a { color: var(--ink); text-decoration: none; }
  .nav-icon {
    width: 30px; height: 22px; margin-right: 16px; flex: none;
    border-radius: 4px; background: var(--icon-fill);
  }

  .recipe-panel {
    position: absolute; left: 137px; top: 427px; width: 247px; height: 283px;
    background: var(--white);
  }
  .recipe-title {
    background: var(--green); color: var(--white);
    font-weight: 700; font-size: 18px; height: 26px; line-height: 26px; padding-left: 20px;
  }
  .recipe-body { padding: 6px 0 0 24px; font-size: 13px; line-height: 15px; }
  .recipe-body h3 { font-size: 13px; font-weight: 400; margin-bottom: 15px; padding-left: 8px; }
  .recipe-body ul { list-style: none; }

  .content {
    position: absolute; left: 442px; top: 72px; width: 638px; height: 624px;
    background: var(--white);
    font-family: "Sorts Mill Goudy", Georgia, serif;
  }
  .page-title { position: absolute; left: 45px; top: 26px; font-size: 25px; font-weight: 400; }
  .gallery { position: absolute; left: 124px; top: 77px; display: flex; gap: 19px; }
  .gallery-photo {
    width: 108px; height: 86px;
    background: linear-gradient(180deg, var(--photo-light) 0%, var(--photo-red) 35%, #b13a2a 75%, var(--photo-light) 100%);
  }
  .copy { position: absolute; left: 124px; top: 198px; width: 480px; font-size: 19px; line-height: 18.4px; }
  .copy p { text-indent: 6px; margin-bottom: 18px; }
</style>
</head>
<body>
  <header class="top-bar"><span class="contact-info">Contact info here</span></header>

  <div class="brand-panel">
    <span class="brand-mark"></span>
    <span class="brand-name">Abuela Rufina's Roasted Dip</span>
  </div>

  <nav class="nav-panel">
    <ul class="nav-list">
      <li class="nav-item"><span class="nav-icon" role="img" aria-label="Small cartoon pepper icon"></span><a href="#">About Us</a></li>
      <li class="nav-item"><span class="nav-icon" role="img" aria-label="Small cartoon pepper icon"></span><a href="#">Testimonials</a></li>
      <li class="nav-item"><span class="nav-icon" role="img" aria-label="Small cartoon pepper icon"></span><a href="#">Locations</a></li>
      <li class="nav-item"><span class="nav-icon" role="img" aria-label="Small cartoon pepper icon"></span><a href="#">Recipes</a></li>
      <li class="nav-item"><span class="nav-icon" role="img" aria-label="Small cartoon pepper icon"></span><a href="#">Buy Online</a></li>
      <li class="nav-item"><span class="nav-icon" role="img" aria-label="Small cartoon pepper icon"></span><a href="#">Contact Us</a></li>
    </ul>
  </nav>

  <aside class="recipe-panel">
    <h2 class="recipe-title">Recipe of the Day</h2>
    <div class="recipe-body">
      <h3>Ingredients:</h3>
      <ul>
        <li>4 cups chopped vine-ripened<br>tomatoes</li>
        <li>2 cups dried black beans,<br>cooked in salted water<br>&nbsp;until tender, cooled (about<br>2 cups)</li>
        <li>1 cup small diced red onions</li>
        <li>1 large fresh jalapeno,<br>&nbsp;seed and cut into small dice</li>
        <li>1/2 cup loosely packed<br>chopped fresh cilantro leaves</li>
        <li>1 tablespoon chopped fresh<br>&nbsp;parsley leaves</li>
      </ul>
    </div>
  </aside>

  <main class="content">
    <h1 class="page-title">About Us</h1>
    <div class="gallery">
      <div class="gallery-photo" role="img" aria-label="Photo of dip jars on a shelf"></div>
      <div class="gallery-photo" role="img" aria-label="Photo of dip jars on a shelf"></div>
      <div class="gallery-photo" role="img" aria-label="Photo of dip jars on a shelf"></div>
    </div>
    <div class="copy">
      <p>Quisque interdum velit non lectus mollis eu dignissim erat euismod. Donec pulvinar, ipsum non iaculis ornare, risus orci placerat elit, ac mattis sapien ligula dictum tellus. Vivamus gravida tempus erat, in eleifend orci volutpat et. Integer varius pulvinar quam, id tempor magna ullamcorper in. Suspendisse quis interdum diam. Aenean et quam arcu. Nullam eget bibendum mauris.</p>
      <p>Quisque interdum velit non lectus mollis eu dignissim erat euismod. Donec pulvinar, ipsum non iaculis ornare, risus orci placerat elit, ac mattis sapien ligula dictum tellus. Vivamus gravida tempus erat, in eleifend orci volutpat et. Integer varius pulvinar quam, id tempor magna</p>
    </div>
  </main>

  <footer class="bottom-bar"><span class="copyright">Copy Right Here</span></footer>
</body>
</html>
```